Young and modern Electrical company working in the commercial arena.

Wanting a business card design thats modern and will last. Maybe Minimalist? Happy to look at changing my logo

Target Market(s)

Builders, Project Managers

Industry/Entity Type

Electrical

Contact Information for Business Card

Name
Address
Phone number
Job title

Logo Text

our name or just the logo i'm open to ideas

Font styles to use
Sans Serif

Requirements
Nice to have
• would like to keep the purple in our current logo. it's kinda unique to our market
Should not have
• Don't want it to be to busy. simple is best i think

```html
<!DOCTYPE html>
<html lang="en">
<head>
<meta charset="UTF-8">
<title>Business Card – Employee Name</title>
<link rel="stylesheet" href="https://fonts.googleapis.com/css2?family=Sarabun:wght@300&display=swap">
<style>
  :root {
    --paper: #ffffff;
    --ink: #000000;
    --purple: #6a05c8;
    --side-grey: #999999;
    --font-main: "Sarabun", Arial, sans-serif;
  }
  * { margin: 0; padding: 0; box-sizing: border-box; }
  html, body {
    width: 1200px;
    height: 686px;
    overflow: hidden;
    background: var(--paper);
  }
  .card {
    position: relative;
    width: 1200px;
    height: 686px;
    background: var(--paper);
    font-family: var(--font-main);
    font-weight: 300;
    color: var(--ink);
    overflow: hidden;
  }
  .side-band {
    position: absolute;
    left: 0; top: 0;
    width: 71px; height: 100%;
    background: var(--side-grey);
  }
  .employee-name {
    position: absolute;
    left: 94px; top: 38px;
    font-size: 58px;
    font-weight: 300;
    line-height: 1.1;
    white-space: nowrap;
  }
  .position {
    position: absolute;
    left: 95px; top: 116px;
    font-size: 20px;
    line-height: 1.2;
  }
  .detail {
    position: absolute;
    left: 71px;
    height: 42px;
    display: flex;
    align-items: center;
    padding-left: 24px;
    font-size: 27px;
    white-space: nowrap;
  }
  .detail::before {
    content: "";
    position: absolute;
    left: 0; top: 0;
    width: 11px; height: 42px;
    background: var(--purple);
  }
  .detail-phone { top: 249px; letter-spacing: 0.5px; }
  .detail-email { top: 322px; }
  .detail-web { top: 394px; }
  .detail-address { top: 603px; word-spacing: 3px; }
  .brand {
    position: absolute;
    right: 60px; top: 318px;
    display: flex;
    align-items: center;
    gap: 16px;
    color: var(--purple);
    font-size: 36px;
    letter-spacing: 2px;
    white-space: nowrap;
  }
  .brand-mark {
    width: 30px; height: 30px;
    background: var(--purple);
  }
</style>
</head>
<body>
  <main class="card">
    <div class="side-band"></div>

    <h1 class="employee-name">EMPLOYEE NAME</h1>
    <p class="position">POSITION</p>

    <p class="detail detail-phone">xxxx xxx xxx</p>
    <p class="detail detail-email">EmployeeName@voltlineelectrical.com.au</p>
    <p class="detail detail-web">www.voltlineelectrical.com.au</p>
    <p class="detail detail-address">Business Street Address | Brackenford | NSW | 2655</p>

    <div class="brand">
      <span class="brand-mark"></span>
      <span class="brand-name">VOLTLINE ELECTRICAL</span>
    </div>
  </main>
</body>
</html>
```